The Perfect Business Card for PineHarbor

I am looking for a business card which beautifully incorporates my logo, reflects my business and looks special, elegant and clean.

```html
<!DOCTYPE html>
<html lang="de">
<head>
<meta charset="utf-8">
<title>PineHarbor Business Card</title>
<link href="https://fonts.googleapis.com/css2?family=Montserrat:wght@400;500;700&display=swap" rel="stylesheet">
<style>
  :root {
    --backdrop: #d9d9d9;
    --card-white: #ffffff;
    --brand-green: #739a3c;
    --brand-green-dark: #5f8430;
    --card-green: #7b9f42;
    --text-dark: #3a3a3a;
    --logo-white: #ffffff;
  }
  * { box-sizing: border-box; margin: 0; padding: 0; }
  html, body {
    width: 1200px; height: 1164px; overflow: hidden;
    background: var(--backdrop);
    font-family: "Montserrat", sans-serif;
  }
  .sheet {
    width: 1200px; height: 1164px;
    display: flex; flex-direction: column;
    align-items: center; justify-content: center; gap: 60px;
  }
  .card {
    width: 860px; height: 490px;
    border-radius: 22px;
    box-shadow: 0 4px 14px rgba(0,0,0,0.18);
    position: relative; overflow: hidden;
  }
  .card-front { background: var(--card-white); }
  .card-back { background: var(--card-green); }

  .brand {
    position: absolute;
    display: flex; align-items: center; gap: 14px;
    font-weight: 500; letter-spacing: 0.5px;
  }
  .brand-dot { border-radius: 50%; flex: none; }
  .card-front .brand { left: 60px; top: 218px; font-size: 38px; color: var(--brand-green-dark); }
  .card-front .brand-dot { width: 18px; height: 18px; background: var(--brand-green-dark); }

  .divider {
    position: absolute; left: 430px; top: 137px;
    width: 2px; height: 216px; background: var(--brand-green);
  }
  .contact { position: absolute; left: 460px; top: 134px; color: var(--text-dark); }
  .contact-name {
    font-weight: 700; font-size: 25px; color: var(--brand-green);
    letter-spacing: 0.5px; line-height: 1.1;
  }
  .contact-role { font-size: 19px; margin-top: 4px; }
  .contact-address { font-size: 19px; line-height: 1.3; margin-top: 24px; }
  .contact-lines { list-style: none; margin-top: 12px; font-size: 19px; line-height: 1.3; }
  .contact-lines li { display: flex; align-items: center; gap: 12px; }
  .contact-lines svg { width: 15px; height: 15px; flex: none; }

  .pattern-field { position: absolute; inset: 0; background: linear-gradient(135deg, #7fa346, #76993e); }
  .card-back .brand { left: 50%; top: 50%; transform: translate(-50%, -50%); font-size: 62px; color: var(--logo-white); gap: 20px; }
  .card-back .brand-dot { width: 26px; height: 26px; background: var(--logo-white); }
</style>
</head>
<body>
<main class="sheet">
  <section class="card card-front" aria-label="Kartenvorderseite">
    <div class="brand"><span class="brand-dot"></span><span class="brand-name">PineHarbor</span></div>
    <div class="divider"></div>
    <div class="contact">
      <p class="contact-name">DR. MIRA HOLMQVIST</p>
      <p class="contact-role">Dipl. Naturheilpraktikerin (TEN)</p>
      <p class="contact-address">Birkenweg 9<br>8045 Zürich</p>
      <ul class="contact-lines">
        <li>
          <svg viewBox="0 0 16 16" aria-hidden="true"><path d="M4 1.5l2.2 3-1.3 1.6a8 8 0 0 0 5 5l1.6-1.3 3 2.2-1.4 2.4C7.5 14.6 1.4 8.5 1.6 2.9z" fill="#739a3c"/></svg>
          <span>+41 (0) 79 555 28 40</span>
        </li>
        <li>
          <svg viewBox="0 0 16 16" aria-hidden="true"><rect x="1" y="3.5" width="14" height="9" fill="#739a3c"/><path d="M1 3.5l7 5 7-5" fill="none" stroke="#fff" stroke-width="1.3"/></svg>
          <span>info@pineharbor.ch</span>
        </li>
        <li>
          <svg viewBox="0 0 16 16" aria-hidden="true"><circle cx="8" cy="8" r="7" fill="#739a3c"/><path d="M1 8h14M8 1c-3 3.5-3 10.5 0 14M8 1c3 3.5 3 10.5 0 14" fill="none" stroke="#fff" stroke-width="1"/></svg>
          <span>www.pineharbor.ch</span>
        </li>
      </ul>
    </div>
  </section>

  <section class="card card-back" aria-label="Kartenrückseite">
    <div class="pattern-field" role="img" aria-label="Faint repeating pattern of the brand symbol in lighter green tones"></div>
    <div class="brand"><span class="brand-dot"></span><span class="brand-name">PineHarbor</span></div>
  </section>
</main>
</body>
</html>
```